" A empresa funciona em um escritório físico, onde os clientes são recebidos para conversar sobre como desejam seu projeto residencial ou comercial. Oferecemos também projetos de decoração, e de instalações, bem como projeto de estrutura. O processo de criação se da tambem pela produção de projetos em 3d. alem da produção do projeto acompanhamos tambem a obra e todo o processo de construção. "

```html
<!DOCTYPE html>
<html lang="pt-BR">
<head>
<meta charset="UTF-8">
<title>Marília Duarte — Papel timbrado</title>
<link href="https://fonts.googleapis.com/css2?family=Montserrat:wght@300;400;500&display=swap" rel="stylesheet">
<style>
  :root {
    --backdrop: #e6e4e1;
    --paper: #ffffff;
    --ink-gray: #8a8a8f;
    --ink-dark: #6d6d72;
    --wash-gray: #f3f3f5;
    --wash-yellow: #fdfbea;
    --accent-yellow: #f7d417;
    --bar-gray: #6f6f74;
  }
  html, body {
    margin: 0;
    width: 1200px;
    height: 1200px;
    overflow: hidden;
    background: var(--backdrop);
    font-family: "Montserrat", sans-serif;
  }
  .letterhead {
    position: absolute;
    left: 288px;
    top: 108px;
    width: 624px;
    height: 984px;
    background: var(--paper);
    overflow: hidden;
    box-shadow: 0 4px 18px rgba(0,0,0,0.12);
  }
  .letterhead__wash {
    position: absolute;
    left: 0;
    right: 0;
    top: 150px;
    height: 620px;
    background:
      linear-gradient(to bottom, var(--paper) 0%, transparent 18%, transparent 82%, var(--paper) 100%),
      linear-gradient(to right, var(--wash-gray) 0%, var(--paper) 50%, var(--wash-yellow) 100%);
  }
  .brand {
    position: absolute;
    left: 52px;
    top: 40px;
    display: flex;
    align-items: center;
    gap: 12px;
  }
  .brand__dot {
    width: 36px;
    height: 36px;
    border-radius: 50%;
    background: var(--accent-yellow);
  }
  .brand__name {
    font-weight: 300;
    font-size: 21px;
    letter-spacing: 1.2px;
    color: var(--ink-gray);
    line-height: 1;
    text-transform: uppercase;
  }
  .brand__tagline {
    font-weight: 400;
    font-size: 7px;
    letter-spacing: 2.2px;
    color: var(--ink-gray);
    text-transform: uppercase;
    margin-top: 5px;
  }
  .contact {
    position: absolute;
    left: 0;
    top: 780px;
    display: flex;
    gap: 22px;
  }
  .contact__bar {
    width: 12px;
    height: 74px;
    background: var(--bar-gray);
  }
  .contact__list {
    list-style: none;
    margin: 2px 0 0;
    padding: 0;
    font-size: 10.5px;
    color: var(--ink-dark);
    line-height: 16px;
  }
  .contact__list li {
    display: flex;
    align-items: flex-start;
    gap: 10px;
  }
  .contact__icon {
    width: 9px;
    height: 9px;
    margin-top: 3.5px;
    flex: none;
  }
  .contact__indent { padding-left: 19px; }
  .corner-band {
    position: absolute;
    right: 0;
    bottom: 0;
    width: 170px;
    height: 14px;
    background: var(--accent-yellow);
  }
</style>
</head>
<body>
  <main class="letterhead">
    <div class="letterhead__wash" role="img" aria-label="Fundo decorativo suave em cinza e amarelo claros"></div>

    <header class="brand">
      <div class="brand__dot"></div>
      <div>
        <div class="brand__name">Marília Duarte</div>
        <div class="brand__tagline">Arquitetura + Interiores</div>
      </div>
    </header>

    <footer class="contact">
      <div class="contact__bar"></div>
      <ul class="contact__list">
        <li>
          <svg class="contact__icon" viewBox="0 0 10 10" aria-hidden="true"><path d="M5 0.5a3.2 3.2 0 0 0-3.2 3.2C1.8 6 5 9.5 5 9.5S8.2 6 8.2 3.7A3.2 3.2 0 0 0 5 0.5z" fill="var(--ink-gray)"/><circle cx="5" cy="3.6" r="1.2" fill="#fff"/></svg>
          <span>Rua das Acácias 48, sala 2</span>
        </li>
        <li class="contact__indent">Centro • Vila Serena • Bahia</li>
        <li>
          <svg class="contact__icon" viewBox="0 0 10 10" aria-hidden="true"><path d="M2.2 0.8l1.6 2-1 1.1c.6 1.3 1.7 2.4 3 3l1.1-1 2 1.6-1 1.7C4.7 9.2.8 5.3 1 1.8z" fill="var(--ink-gray)"/></svg>
          <span>(00) 90000-1234 • 90000-5678</span>
        </li>
        <li>
          <svg class="contact__icon" viewBox="0 0 10 10" aria-hidden="true"><rect x="0.5" y="2" width="9" height="6.5" rx="0.8" fill="var(--ink-gray)"/><path d="M1 2.6L5 5.6 9 2.6" fill="none" stroke="#fff" stroke-width="0.9"/></svg>
          <span>marilia.arquiteta@exemplo.com</span>
        </li>
      </ul>
    </footer>

    <div class="corner-band"></div>
  </main>
</body>
</html>
```